Divorce marketing brochure - Which will include a toy ball and chain as a gimick

A single page marketing enclosure which includes a toy ball and chain to be given to lawyers. I want to convey the following messages:

1. We pay a 1/3 referral fee;
2. We solve difficult problems.

Examples of problems solved:
*Litigation of complex property, custody, support and parenting time issues;
*Protection (or invasion) of personal injury proceeds in divorce;
*Distribution of consortium proceeds in divorce;
*Pre-nuptial and Post-nuptial agreements.
*Settlements
*Reduce conflict

A sample of the toy ball and chain enclosure can be viewed here:

My website is www.thesplitcounsel.com (currently being updated - who's isn't?)

http://www.shopvexto.com/Orbel-Trinkets-Inc-Convict-Shackle/dp/K7QX3MZP21/ref=sr_1_9?ie=UTF8&qid=1311011554&sr=8-9

Target Market(s)

Personal Injury Attorneys

Industry/Entity Type

Marketing

Requirements
Must have
• Call to action:

www.thesplitcounsel.com
1-877-HIRE-TEAM
248-555-7182
Marcus@brevanlegal.com
Nice to have
• I want this campaign to stand out. Different is good. I am a divorce lawyer marketing to personal injury attorneys (and some others) for divorce referrals. (No one forgets the girl with red hair and braces) I want the campaign to be remembered without being offensive.
Should not have

```html
<!DOCTYPE html>
<html lang="en">
<head>
<meta charset="utf-8">
<title>Referral Fee Brochure</title>
<link href="https://fonts.googleapis.com/css2?family=Anton&family=Oswald:wght@300;400&family=Roboto+Condensed:wght@400;700&display=swap" rel="stylesheet">
<style>
  :root {
    --red: #e31b23;
    --pink: #f6b9bb;
    --paper: #ffffff;
    --yellow: #ffe600;
    --ink: #111111;
    --charcoal: #1a1a1a;
    --steel: #6d6d6d;
  }
  * { margin: 0; padding: 0; box-sizing: border-box; }
  html, body { width: 846px; height: 1200px; overflow: hidden; background: var(--paper); }
  .brochure {
    position: relative;
    width: 846px;
    height: 1200px;
    overflow: hidden;
    background: linear-gradient(to bottom, var(--red) 0px, var(--red) 300px, var(--pink) 480px, var(--paper) 640px);
  }
  .headline {
    position: absolute;
    left: 0; width: 100%;
    text-align: center;
    font-family: "Anton", Impact, sans-serif;
    color: var(--yellow);
    text-shadow: 4px 4px 0 var(--ink);
    letter-spacing: 1px;
    line-height: 1;
  }
  .headline--fee { top: 18px; font-size: 112px; }
  .headline--referral { top: 126px; font-size: 112px; }
  .divider {
    position: absolute; left: 40px; right: 40px; top: 286px;
    height: 2px; background: var(--yellow);
  }
  .tagline {
    position: absolute; top: 298px; left: 0; width: 100%;
    text-align: center;
    font-family: "Anton", Impact, sans-serif;
    font-size: 50px; line-height: 1;
    color: var(--yellow);
    text-shadow: 3px 3px 0 var(--ink);
    letter-spacing: 1px;
  }
  .problems {
    position: absolute; left: 40px; top: 372px; width: 380px;
    list-style: none;
    font-family: "Roboto Condensed", Arial Narrow, sans-serif;
    font-weight: 700; font-size: 25px; line-height: 1.14;
    color: var(--ink);
  }
  .problems li { position: relative; padding-left: 20px; margin-bottom: 4px; }
  .problems li::before { content: "•"; position: absolute; left: 0; }
  .pointer { position: absolute; left: 366px; top: 384px; width: 460px; height: 446px; }
  .pointer-label {
    position: absolute; right: 48px; top: 470px;
    text-align: right;
    font-family: "Oswald", Arial Narrow, sans-serif;
    font-weight: 300; font-size: 60px; line-height: 1.2;
    color: var(--ink);
  }
  .firm-mark {
    position: absolute; left: 60px; top: 1048px; width: 346px; height: 104px;
    background: var(--ink);
    display: flex; align-items: center; justify-content: center; gap: 14px;
  }
  .firm-mark__dot { width: 26px; height: 26px; border-radius: 50%; background: var(--paper); }
  .firm-mark__name {
    font-family: "Roboto Condensed", Arial Narrow, sans-serif;
    font-weight: 400; font-size: 30px; color: var(--paper);
  }
  .shackle {
    position: absolute; left: 0; top: 1120px; width: 540px; height: 80px;
    background: linear-gradient(to bottom, var(--steel), var(--charcoal));
    border-top-right-radius: 40px;
  }
  .cta {
    position: absolute; left: 476px; top: 874px; width: 370px; height: 370px;
    border-radius: 50%; background: var(--charcoal);
    display: flex; flex-direction: column; align-items: center; justify-content: flex-start;
    padding-top: 70px;
    font-family: "Roboto Condensed", Arial Narrow, sans-serif;
    color: var(--paper); text-align: center;
  }
  .cta__title { font-weight: 700; font-size: 32px; line-height: 1.25; }
  .cta__web { font-weight: 400; font-size: 29px; line-height: 1.3; }
  .cta__toll { font-weight: 700; font-size: 32px; line-height: 1.25; color: var(--yellow); }
  .cta__phone { font-weight: 700; font-size: 32px; line-height: 1.25; }
  .cta__email { font-weight: 400; font-size: 27px; line-height: 1.3; }
</style>
</head>
<body>
<main class="brochure">
  <h1 class="headline headline--fee">WE PAY A 1/3</h1>
  <h1 class="headline headline--referral">REFERRAL FEE</h1>
  <div class="divider"></div>
  <h2 class="tagline">WE SOLVE DIFFICULT PROBLEMS</h2>

  <ul class="problems">
    <li>Litigation of complex property, custody, support and parenting time issues</li>
    <li>Protection (or invasion) of personal injury proceeds in divorce</li>
    <li>Distribution of consortium proceeds in divorce</li>
    <li>Pre-nuptial and Post-nuptial agreements</li>
    <li>Settlements</li>
    <li>Reduce conflict</li>
  </ul>

  <svg class="pointer" viewBox="0 0 460 446" aria-hidden="true">
    <polygon points="0,222 152,0 152,72 452,72 452,372 152,372 152,446" fill="#ffe600"/>
  </svg>
  <p class="pointer-label">EXAMPLES<br>OF PROBLEMS<br>SOLVED:</p>

  <div class="firm-mark">
    <span class="firm-mark__dot"></span>
    <span class="firm-mark__name">The Brevan Law Firm</span>
  </div>

  <div class="shackle" role="img" aria-label="Toy ball and chain with shackle cuff"></div>

  <section class="cta">
    <p class="cta__title">CALL TO ACTION:</p>
    <p class="cta__web">www.thesplitcounsel.com</p>
    <p class="cta__toll">1-877-HIRE-TEAM</p>
    <p class="cta__phone">248-555-7182</p>
    <p class="cta__email">Marcus@brevanlegal.com</p>
  </section>
</main>
</body>
</html>
```